Redesign Website for Corvane Blaze

I have an existing website on https://www.corvaneblaze-demo.com.au/ and would like to have this redesigned professionally with new content (please refer to word document). We are fire protection engineers providing fire services design expertise and engineering design to a range of different clients.

We also provide drafting services to clients in the form of completing final commissioning documentation such as 'as-installed' drawings and fire services block plans to ensure compliance with the building code and relevant Australian Standards.

Target Market(s)

Builders, Architects, Consultants, Project Managers

Industry/Entity Type

Engineering Consultant

Coding

Coded - Design and coding required

Number of Pages Required

4 page

Font styles to use
Sans Serif

Requirements
Must have
• Home and about Page, fire services design page, fire block plans page, contact us page (4 Pages).

The website colour choice must match or compliment the new company logo.
Nice to have
• Quality photos of fire services installations in buildings to Australian Standards.

A website similar to this would be ideal http://quorbelflame-demo.com.au
Should not have
• Stolen licensed photos

```html
<!DOCTYPE html>
<html lang="en">
<head>
<meta charset="utf-8">
<title>Corvane Blaze – Fire Services Drawings and Block Plans</title>
<link href="https://fonts.googleapis.com/css2?family=Roboto:wght@400;500;700;900&display=swap" rel="stylesheet">
<style>
:root{
  --orange:#f07f12;
  --orange-dark:#d96a05;
  --ink:#1c1c1c;
  --body:#444;
  --muted:#777;
  --line:#d9d9d9;
  --white:#fff;
  --grey-band:#e9eaec;
  --beige:#f1dcc2;
  --black:#0b0b0b;
}
*{box-sizing:border-box;margin:0;padding:0}
html,body{width:1200px;height:3816px;overflow:hidden}
body{font-family:"Roboto",Arial,sans-serif;color:var(--body);background:var(--white);position:relative}
a{color:inherit;text-decoration:none}
.abs{position:absolute}
.btn{display:inline-block;background:var(--orange);color:var(--white);font-size:15px;font-weight:500;padding:13px 28px;border-radius:2px}

/* header */
.site-header{position:absolute;left:0;top:0;width:1200px;height:44px;background:var(--white);display:flex;align-items:center;padding:0 88px;z-index:2}
.brand{display:flex;align-items:center;gap:8px;font-weight:700;font-size:16px;color:var(--orange);letter-spacing:.5px}
.brand-dot{width:16px;height:16px;background:var(--orange);border-radius:50%}
.main-nav{display:flex;gap:40px;margin-left:auto;font-size:14px;color:var(--ink)}
.main-nav .active{color:var(--orange)}
.search-icon{margin-left:50px}
.login{margin-left:40px;background:var(--orange);color:#fff;font-size:13px;padding:7px 26px;border-radius:2px}

/* hero */
.hero{position:absolute;left:0;top:44px;width:1200px;height:668px;background:linear-gradient(100deg,#c8ccd0 0%,#e8e8e6 35%,#d8d4cf 55%,#9aa0a5 100%)}
.hero-photo{position:absolute;inset:0;background:linear-gradient(90deg,rgba(90,110,140,.45) 0%,rgba(200,60,50,.25) 30%,rgba(0,0,0,0) 45%,rgba(40,40,40,.35) 100%)}
.hero-copy{position:absolute;left:586px;top:222px;width:500px;color:#fff}
.hero-copy h1{font-size:40px;font-weight:900;letter-spacing:.5px}
.hero-copy h2{font-size:30px;font-weight:700;color:var(--orange);margin-top:10px}
.hero-copy p{font-size:14px;line-height:22px;margin-top:14px;width:440px}
.hero-copy .btn{margin-top:26px}
.slider-arrow{position:absolute;top:350px}

/* about */
.about{position:absolute;left:0;top:712px;width:1200px;height:408px}
.section-title{font-size:34px;font-weight:700;color:var(--ink)}
.about-copy{position:absolute;left:88px;top:124px;width:470px}
.about-copy p{font-size:15px;line-height:26px;margin-top:24px;color:var(--body)}
.about-copy .btn{margin-top:22px}
.about-photo{position:absolute;left:704px;top:72px;width:360px;height:248px;background:linear-gradient(120deg,#d9dee2,#b9c3cb 50%,#b2402e 100%)}

/* block plans */
.block-plans{position:absolute;left:0;top:1120px;width:1200px;height:672px;background:linear-gradient(180deg,#e4e6e9,#d3d7dc 60%,#e7e8ea)}
.block-plans .section-title{position:absolute;top:62px;width:100%;text-align:center;font-size:32px}
.block-plans .intro{position:absolute;top:136px;left:170px;width:860px;text-align:center;font-size:14px;line-height:22px;color:#333}
.plan-card{position:absolute;top:260px;width:304px;height:340px;background:var(--white);text-align:center;box-shadow:0 3px 10px rgba(0,0,0,.08)}
.plan-card svg{margin-top:24px}
.plan-card h3{font-size:16px;font-weight:500;color:var(--ink);margin-top:14px}
.plan-card p{font-size:13px;line-height:20px;color:var(--muted);margin:12px 26px 0}
.read-more{position:absolute;bottom:28px;left:0;width:100%;font-size:14px;color:var(--orange)}

/* drawings */
.drawings{position:absolute;left:0;top:1792px;width:1200px;height:428px}
.drawings-photo{position:absolute;left:88px;top:88px;width:412px;height:260px;background:linear-gradient(110deg,#9a1f18,#c8473a 40%,#b8bfc7 70%,#e0e2e4)}
.drawings-copy{position:absolute;left:648px;top:88px;width:460px}
.drawings-copy .section-title{font-size:34px}
.drawings-copy p{font-size:15px;line-height:25px;margin-top:24px}
.drawings-copy .btn{margin-top:26px}

/* testimonials */
.testimonials{position:absolute;left:0;top:2220px;width:1200px;height:600px;background:linear-gradient(180deg,#efd6b8,#f3e4d1 60%,#eed8bd)}
.testimonials .section-title{position:absolute;top:72px;left:320px;font-size:38px}
.quote-card{position:absolute;top:148px;width:320px;height:392px;background:var(--white);text-align:center;padding-top:34px}
.avatar{width:104px;height:104px;border-radius:50%;margin:0 auto;background:radial-gradient(circle at 50% 40%,#8ba3c1,#2d4b77)}
.quote-card h4{font-size:15px;font-weight:500;color:var(--orange);margin-top:28px}
.quote-card p{font-size:14px;line-height:22px;color:#333;margin:14px 32px 0}
.stars{display:flex;justify-content:center;gap:10px;margin-top:22px}

/* call back */
.callback{position:absolute;left:0;top:2820px;width:1200px;height:660px}
.callback .section-title{position:absolute;left:88px;top:84px;font-size:38px;font-weight:500}
.field{position:absolute;left:88px;width:432px;height:46px;border:1px solid var(--line);background:#f7f7f7;font-size:14px;padding:14px 16px;color:#555}
.send{position:absolute;left:216px;top:452px;width:176px;height:46px;background:var(--orange);color:#fff;font-size:15px;font-weight:500;text-align:center;line-height:46px}
.map-box{position:absolute;left:600px;top:92px;width:512px;height:408px;background:linear-gradient(160deg,#cfe5f2 0%,#aad3e8 30%,#d8c99b 55%,#c7d8a8 75%,#aad3e8 100%);border:1px solid #ddd}
.map-tabs{position:absolute;left:0;top:0;display:flex;background:#fff;font-size:14px;box-shadow:0 1px 3px rgba(0,0,0,.2)}
.map-tabs span{padding:8px 16px}
.map-tabs span+span{color:#777}

/* footer */
.site-footer{position:absolute;left:0;top:3480px;width:1200px;height:280px;background:var(--black);color:#ddd}
.footer-brand{position:absolute;left:88px;top:70px}
.footer-about{position:absolute;left:88px;top:120px;width:260px;font-size:14px;line-height:22px;color:#cfcfcf}
.socials{position:absolute;left:88px;top:200px;display:flex;gap:14px}
.socials span{width:32px;height:32px;border-radius:50%;background:var(--orange)}
.footer-col{position:absolute;top:70px}
.footer-col h5{font-size:15px;font-weight:500;color:#fff;letter-spacing:.5px}
.footer-col ul{list-style:none;margin-top:30px}
.footer-col li{font-size:14px;color:#cfcfcf;margin-bottom:17px}
.contact-line{display:flex;align-items:center;gap:16px;font-size:14px;color:#cfcfcf;margin-top:26px}
.contact-line .ico{width:34px;height:34px;border-radius:50%;background:var(--orange);display:flex;align-items:center;justify-content:center}
.copyright-bar{position:absolute;left:0;top:3760px;width:1200px;height:56px;background:var(--orange);color:#fff;font-size:14px;text-align:center;line-height:56px}
</style>
</head>
<body>

<header class="site-header">
  <a class="brand" href="#"><span class="brand-dot"></span>CORVANE BLAZE</a>
  <nav class="main-nav">
    <a class="active" href="#">Home</a>
    <a href="#">About</a>
    <a href="#">Fire Services Plans</a>
    <a href="#">Fire Block Plans</a>
    <a href="#">Contact us</a>
  </nav>
  <svg class="search-icon" width="18" height="18" viewBox="0 0 18 18"><circle cx="7.5" cy="7.5" r="6" fill="none" stroke="#333" stroke-width="2"/><line x1="12" y1="12" x2="17" y2="17" stroke="#333" stroke-width="2"/></svg>
  <a class="login" href="#">Log in</a>
</header>

<section class="hero">
  <div class="hero-photo" role="img" aria-label="Engineer inspecting a red fire extinguisher mounted on a wall while holding a clipboard"></div>
  <svg class="slider-arrow" style="left:20px" width="14" height="22" viewBox="0 0 14 22"><polyline points="11,2 3,11 11,20" fill="none" stroke="#fff" stroke-width="3"/></svg>
  <svg class="slider-arrow" style="right:20px" width="14" height="22" viewBox="0 0 14 22"><polyline points="3,2 11,11 3,20" fill="none" stroke="#fff" stroke-width="3"/></svg>
  <div class="hero-copy">
    <h1>CORVANE BLAZE</h1>
    <h2>Fire Services Drawings and Block Plans</h2>
    <p>We pride ourselves in our ability to meet the demands of our clients and our ability to consistently deliver.</p>
    <a class="btn" href="#">Learn more</a>
  </div>
</section>

<section class="about">
  <div class="about-copy">
    <h2 class="section-title">ABOUT CORVANE BLAZE</h2>
    <p>We pride ourselves in our ability to meet the demands of our clients and our ability to consistently uphold our 3 key business values in providing our services at quick turnaround, quality service at competitive pricing.</p>
    <a class="btn" href="#">Learn more</a>
  </div>
  <div class="about-photo" role="img" aria-label="Technician in a hard hat servicing a red fire panel"></div>
</section>

<section class="block-plans">
  <h2 class="section-title">Fire Block Plans</h2>
  <p class="intro">We can can also assist you with the preparation of final commissioning documentation as required to achieve with relevant Australian Standards. Some of the services we provide (but not limited to) include:</p>
  <svg class="slider-arrow" style="left:20px;top:330px" width="12" height="20" viewBox="0 0 12 20"><polyline points="10,2 2,10 10,18" fill="none" stroke="#222" stroke-width="3"/></svg>
  <svg class="slider-arrow" style="right:20px;top:330px" width="12" height="20" viewBox="0 0 12 20"><polyline points="2,2 10,10 2,18" fill="none" stroke="#222" stroke-width="3"/></svg>

  <article class="plan-card" style="left:88px">
    <svg width="92" height="96" viewBox="0 0 92 96"><polygon points="46,2 88,25 88,71 46,94 4,71 4,25" fill="var(--orange)"/><polygon points="46,30 64,62 28,62" fill="none" stroke="#fff" stroke-width="4"/><line x1="46" y1="42" x2="46" y2="52" stroke="#fff" stroke-width="4"/></svg>
    <h3>Zone Block Plans</h3>
    <p>AS1670.1 requires all automatic smoke detection and alarm systems to incorporate a Zone Block Plan.</p>
    <a class="read-more" href="#">Read more &nbsp;›</a>
  </article>

  <article class="plan-card" style="left:448px">
    <svg width="92" height="96" viewBox="0 0 92 96"><polygon points="46,2 88,25 88,71 46,94 4,71 4,25" fill="var(--orange)"/><polygon points="28,40 38,40 50,30 50,66 38,56 28,56" fill="#fff"/><path d="M56 38 q8 10 0 20 M62 32 q14 16 0 32" fill="none" stroke="#fff" stroke-width="3"/></svg>
    <h3>EWIS / SSISEP Block Plans</h3>
    <p>requires an Emergency Warning and Intercom System (EWIS) / Sound System and Intercom System...</p>
    <a class="read-more" href="#">Read more &nbsp;›</a>
  </article>

  <article class="plan-card" style="left:808px">
    <svg width="92" height="96" viewBox="0 0 92 96"><polygon points="46,2 88,25 88,71 46,94 4,71 4,25" fill="var(--orange)"/><rect x="34" y="28" width="24" height="8" fill="#fff"/><rect x="42" y="36" width="8" height="14" fill="#fff"/><circle cx="46" cy="56" r="7" fill="#fff"/><path d="M30 66 l-4 6 M46 68 v8 M62 66 l4 6" stroke="#fff" stroke-width="3"/></svg>
    <h3>Sprinkler Block Plans</h3>
    <p>A Sprinkler Block Plan details the layout of the building and the configuration of the installed Sprinkler</p>
    <a class="read-more" href="#">Read more &nbsp;›</a>
  </article>
</section>

<section class="drawings">
  <div class="drawings-photo" role="img" aria-label="Two engineers reviewing a fire services installation beside red equipment"></div>
  <div class="drawings-copy">
    <h2 class="section-title">FIRE SERVICES DRAWINGS</h2>
    <p>Fire Services Drawings Corvane Blaze can assist with the preparation of the design and specification for the upgrade or installation or new fire safety systems to achieve compliance with the National Construction Code (NCC), Council Fire Orders or Fire Engineering Reports.</p>
    <a class="btn" href="#">Learn more</a>
  </div>
</section>

<section class="testimonials">
  <h2 class="section-title">OUR TESTIMONIALS</h2>
  <article class="quote-card" style="left:232px">
    <div class="avatar" role="img" aria-label="Portrait of client John Smith"></div>
    <h4>JOHN SMITH</h4>
    <p>Lorem ipsum dolor sit amet, consectetur adipiscing elit, sed do eiusmod tempor incididunt ut labore et dolore magna.</p>
    <div class="stars">
      <svg width="22" height="22" viewBox="0 0 24 24"><polygon points="12,1 15,9 23,9 17,14 19,23 12,18 5,23 7,14 1,9 9,9" fill="var(--orange)"/></svg>
      <svg width="22" height="22" viewBox="0 0 24 24"><polygon points="12,1 15,9 23,9 17,14 19,23 12,18 5,23 7,14 1,9 9,9" fill="#111"/></svg>
      <svg width="22" height="22" viewBox="0 0 24 24"><polygon points="12,1 15,9 23,9 17,14 19,23 12,18 5,23 7,14 1,9 9,9" fill="#111"/></svg>
    </div>
  </article>
  <article class="quote-card" style="left:632px">
    <div class="avatar" role="img" aria-label="Portrait of client John Doe"></div>
    <h4>JOHN DEO</h4>
    <p>Lorem ipsum dolor sit amet, consectetur adipiscing elit, sed do eiusmod tempor incididunt ut labore et dolore magna.</p>
    <div class="stars">
      <svg width="22" height="22" viewBox="0 0 24 24"><polygon points="12,1 15,9 23,9 17,14 19,23 12,18 5,23 7,14 1,9 9,9" fill="var(--orange)"/></svg>
      <svg width="22" height="22" viewBox="0 0 24 24"><polygon points="12,1 15,9 23,9 17,14 19,23 12,18 5,23 7,14 1,9 9,9" fill="var(--orange)"/></svg>
      <svg width="22" height="22" viewBox="0 0 24 24"><polygon points="12,1 15,9 23,9 17,14 19,23 12,18 5,23 7,14 1,9 9,9" fill="#111"/></svg>
    </div>
  </article>
</section>

<section class="callback">
  <h2 class="section-title">REQUEST A CALL BACK</h2>
  <div class="field" style="top:170px">Name</div>
  <div class="field" style="top:234px">Email</div>
  <div class="field" style="top:298px">Phone contact</div>
  <div class="field" style="top:362px">Detail your request</div>
  <div class="send">SEND MESSAGE</div>
  <div class="map-box" role="img" aria-label="Map of Australia with a location pin on the south-east coast">
    <div class="map-tabs"><span>Map</span><span>Satellite</span></div>
  </div>
</section>

<footer class="site-footer">
  <div class="footer-brand brand"><span class="brand-dot"></span>CORVANE BLAZE</div>
  <p class="footer-about">Lorem ipsum dolor sit amet, consectetur adipiscing elit sed do eiusmod tempor incididunt gravida risus commodo.</p>
  <div class="socials"><span></span><span></span><span></span></div>
  <div class="footer-col" style="left:550px">
    <h5>INFORMATION</h5>
    <ul>
      <li>Home</li><li>About</li><li>Fire Services Plans</li><li>Fire Block Plans</li><li>Contact us</li>
    </ul>
  </div>
  <div class="footer-col" style="left:868px">
    <h5>CONTACT US</h5>
    <div class="contact-line"><span class="ico"><svg width="16" height="16" viewBox="0 0 24 24"><path d="M6 2 l4 0 l2 5 l-3 2 q2 5 6 6 l2-3 l5 2 l0 4 q0 4-4 4 q-16-2-16-16 q0-4 4-4z" fill="#fff"/></svg></span>+614 55 210 394</div>
    <div class="contact-line"><span class="ico"><svg width="16" height="12" viewBox="0 0 16 12"><rect x="0" y="0" width="16" height="12" fill="#fff"/><polyline points="0,0 8,7 16,0" fill="none" stroke="var(--orange)" stroke-width="1.5"/></svg></span>info@corvaneblaze-demo.com.au</div>
  </div>
</footer>
<div class="copyright-bar">©Copyright 2021 Corvane Blaze All rights reserved</div>

</body>
</html>
```